Tellwick Asset Management - Corporate Letter Head Project

Looking for a classy design based on our current logo. Please find current logo source file in files. With our color scheme.

Target Market(s)

We're an investment firm, the letterhead needs to look professional and attractive to clients.

Industry/Entity Type

Hedgefund

Colors
0054AA
0677BA
7BADD7
CADEEF
E8F1F8

Requirements
Must have
• Our logo, address, phone number, and email

```html
<!DOCTYPE html>
<html lang="en">
<head>
<meta charset="utf-8">
<title>Tellwick Asset Management – Letterhead</title>
<link href="https://fonts.googleapis.com/css2?family=Playfair+Display:wght@400;700&family=Open+Sans:wght@400;600&family=Raleway:wght@600&display=swap" rel="stylesheet">
<style>
:root{
  --navy:#212c4a;
  --paper:#ffffff;
  --ink:#1f2a47;
  --muted:#7c7f86;
  --canvas:#ffffff;
}
*{margin:0;padding:0;box-sizing:border-box}
html,body{width:1200px;height:1074px;overflow:hidden;background:var(--canvas)}
body{position:relative;font-family:'Open Sans',sans-serif;color:var(--ink)}

.sheet{position:absolute;width:340px;height:481px}
.sheet--framed{background:var(--navy)}
.sheet--framed .card{position:absolute;left:7px;top:11px;right:7px;bottom:11px;background:var(--paper);border-radius:4px}
.sheet--reverse{background:var(--paper);box-shadow:3px 4px 6px rgba(0,0,0,.35)}
.sheet--reverse .card{position:absolute;left:7px;top:11px;right:7px;bottom:11px;background:var(--navy);border-radius:4px}

.sheet--small{transform:scale(.71);transform-origin:0 0}

.brand{position:absolute;left:32px;top:26px;width:70px;text-align:center;font-family:'Playfair Display',serif;color:var(--navy)}
.brand__square{display:block;width:18px;height:18px;border:1px solid var(--navy);margin:0 auto 6px}
.brand__name{display:block;font-size:7.4px;line-height:1;white-space:nowrap}
.brand__sub{display:block;font-size:3.6px;letter-spacing:2.2px;margin-top:1px;white-space:nowrap}

.address{position:absolute;left:31px;bottom:11px;font-family:'Playfair Display',serif;font-size:5.2px;line-height:9px;text-transform:uppercase;color:var(--ink)}
.website{position:absolute;right:26px;bottom:11px;font-family:'Playfair Display',serif;font-weight:700;font-size:4.6px;line-height:9px;color:var(--ink)}

.mark{position:absolute;left:50%;top:50%;transform:translate(-50%,-50%);text-align:center;color:#fff;font-family:'Playfair Display',serif}
.mark__square{display:block;width:28px;height:28px;border:1px solid #fff;margin:0 auto 5px}
.mark__name{font-size:5px;letter-spacing:1.5px;white-space:nowrap}

.recipient{position:absolute;left:32px;top:106px;width:270px}
.recipient__name{font-family:'Open Sans',sans-serif;font-weight:600;font-size:7.4px;color:var(--ink)}
.recipient__lines{margin-top:4px;font-size:4.8px;line-height:7.4px;color:var(--muted)}
.letter-date{position:absolute;right:0;bottom:0;font-size:4.8px;line-height:7.4px;color:var(--muted)}
.body-copy{position:absolute;left:32px;top:179px;width:270px;font-size:5.1px;line-height:7.5px;color:var(--muted);text-align:justify}
.body-copy p{margin-bottom:7.5px}
.signature{position:absolute;left:32px;top:395px}
.signature__name{font-family:'Raleway',sans-serif;font-weight:600;font-size:6.6px;color:var(--ink)}
.signature__role{font-size:4.8px;color:var(--muted);margin-top:3px}
</style>
</head>
<body>

<!-- Top row: front and reverse -->
<div class="sheet sheet--framed sheet--small" style="left:257px;top:123px">
  <div class="card">
    <div class="brand"><span class="brand__square"></span><span class="brand__name">TELLWICK ASSET</span><span class="brand__sub">MANAGEMENT</span></div>
    <div class="address">Address, Street Number,<br>PO Box 1234, City, Tel.: +123 456 789<br>Email: mail@tellwickasset.com</div>
    <div class="website">www.tellwickasset.com</div>
  </div>
</div>
<div class="sheet sheet--reverse sheet--small" style="left:700px;top:123px">
  <div class="card"><div class="mark"><span class="mark__square"></span><span class="mark__name">TELLWICK</span></div></div>
</div>

<!-- Bottom row: front, reverse, filled letter -->
<div class="sheet sheet--framed" style="left:38px;top:556px">
  <div class="card">
    <div class="brand"><span class="brand__square"></span><span class="brand__name">TELLWICK ASSET</span><span class="brand__sub">MANAGEMENT</span></div>
    <div class="address">Address, Street Number,<br>PO Box 1234, City, Tel.: +123 456 789<br>Email: mail@tellwickasset.com</div>
    <div class="website">www.tellwickasset.com</div>
  </div>
</div>

<div class="sheet sheet--reverse" style="left:391px;top:556px">
  <div class="card"><div class="mark"><span class="mark__square"></span><span class="mark__name">TELLWICK</span></div></div>
</div>

<div class="sheet sheet--framed" style="left:754px;top:557px">
  <div class="card">
    <div class="brand"><span class="brand__square"></span><span class="brand__name">TELLWICK ASSET</span><span class="brand__sub">MANAGEMENT</span></div>
    <div class="recipient">
      <div class="recipient__name">Name Surname</div>
      <div class="recipient__lines">Senior Executive<br>123 Anywhere St., Any City<br>hello@samplemailbox.com<br>+123-456-7890</div>
      <div class="letter-date">Date, 10 September, 2030</div>
    </div>
    <div class="body-copy">
      <p>Lorem ipsum dolor sit amet, consectetur adipisicing elit, sed do eiusmod tempor incididunt ut labore et dolore magna aliqua. Ut enim ad minim veniam, quis nostrud exercitation ullamco laboris nisi ut aliquip ex ea commodo consequat. Duis aute irure dolor in reprehenderit in voluptate velit esse cillum dolore eu fugiat nulla pariatur. Excepteur sint occaecat cupidatat non proident, sunt in culpa qui officia deserunt mollit anim id est laborum. Sed ut perspiciatis unde omnis iste natus error sit voluptatem accusantium doloremque laudantium, totam rem aperiam, eaque ipsa quae ab illo inventore veritatis et quasi architecto beatae vitae dicta sunt explicabo. Nemo enim ipsam voluptatem quia voluptas sit aspernatur aut odit aut fugit, sed quia consequuntur magni dolores eos qui ratione voluptatem sequi nesciunt. Neque porro voluptatem sequi nesciunt. Nemo enim ipsam voluptatem quia voluptas.</p>
      <p>Lorem ipsum dolor sit amet, consectetur adipisicing elit, sed do eiusmod tempor incididunt ut labore et dolore magna aliqua. Ut enim ad minim veniam, quis nostrud exercitation ullamco laboris nisi ut aliquip ex ea commodo consequat. Duis aute irure dolor in reprehenderit in voluptate velit esse cillum dolore eu fugiat nulla pariatur. Excepteur sint occaecat cupidatat non proident, sunt in culpa qui officia deserunt mollit anim id est laborum. Sed ut perspiciatis unde omnis iste natus error sit voluptatem accusantium doloremque laudantium, totam rem aperiam, eaque ipsa quae ab illo inventore veritatis et quasi architecto beatae vitae dicta sunt explicabo. Nemo enim ipsam voluptatem quia voluptas sit aspernatur aut odit aut.</p>
      <p>Lorem ipsum dolor sit amet, consectetur adipisicing elit, sed do eiusmod tempor incididunt ut labore et dolore magna aliqua. Ut enim ad minim veniam, quis nostrud exercitation ullamco laboris nisi ut aliquip ex ea commodo consequat.</p>
    </div>
    <div class="signature"><div class="signature__name">NAME SURNAME</div><div class="signature__role">General Manager</div></div>
    <div class="address">Address, Street Number,<br>PO Box 1234, City, Tel.: +123 456 789<br>Email: mail@tellwickasset.com</div>
    <div class="website">www.tellwickasset.com</div>
  </div>
</div>

</body>
</html>
```